VividoCanta hobbyist website to display and sell art.

A website to promote my artwork with the ability to sell and show many examples of my work . I have called my small hobbyist art selling business 'VividoCanta' i. Some works can be seen in my Facebook page VividoCanta . It needs to be creative and fit with my style of art. It needs to show passion!!!
I also have a business website www.brightlanewayworks.example which gives you an indication of my choice of design style.
The website will need to display art under headings of Landscape ; Portraits and Other Works ; tell the client about me the artist and my inspiration; commission works and sell art ;
My tagline is original art with colour, passion and movement. My style is impressionistic and expressive contemporary not traditional and realism.
I paint in Acrylic , Pastels and Oils.
I would like to collect information on people visiting the site so I can send them information on exhibitions; new work etc further down the track ; the ability to build landing pages ? A photo of me?
Updates

Target Market(s)

The Home Art/ Craft market- buyers of affordable but original works ; double income no kids , cool trendy lovers of abstract / impressionistic art with lots of vivid colour! For gifts or something you love for your home or office. Perhaps galleries.

Industry/Entity Type

Artists

Coding

Coded - Design and coding required

Number of Pages Required

4 page

Font styles to use
Sans Serif
Other font styles liked:
• Calibri, Comic Sans or some other fun

Requirements
Must have
• Passion , professional but modern and casual; fast and simple to use and update; clear messages ; vivid colour.
• A gallery;
• The colour will probably need to go with different coloured works as I update paintings
Nice to have
• A payment option
• Something really different and catchy
• Landing pages
Should not have
• A boring approach;

```html
<!DOCTYPE html>
<html lang="en">
<head>
<meta charset="utf-8">
<title>VividoCanta – Contact</title>
<link rel="stylesheet" href="https://fonts.googleapis.com/css2?family=Lato:wght@400;700;900&display=swap">
<style>
  :root {
    --teal: #2abbb5;
    --ink: #000000;
    --paper: #ffffff;
    --hint: #8a8a8a;
    --paint-deep: #0f2a4a;
    --paint-blue: #1c6fa8;
    --paint-aqua: #2bb7c4;
    --paint-ember: #c9783a;
    --paint-dark: #1b1a26;
  }
  * { box-sizing: border-box; margin: 0; padding: 0; }
  html, body {
    width: 1200px;
    height: 900px;
    overflow: hidden;
    background: var(--paper);
    font-family: "Lato", sans-serif;
    color: var(--ink);
  }
  .page { position: relative; width: 1200px; height: 900px; }

  .side-art {
    position: absolute;
    top: 0;
    width: 204px;
    height: 900px;
    background: linear-gradient(180deg,
      var(--paint-deep) 0%,
      var(--paint-blue) 18%,
      var(--paint-ember) 30%,
      var(--paint-aqua) 45%,
      var(--paint-blue) 58%,
      var(--paint-aqua) 66%,
      var(--paint-dark) 80%,
      var(--paint-ember) 92%,
      var(--paint-dark) 100%);
  }
  .side-art--left { left: 0; }
  .side-art--right { left: 1005px; width: 195px; }

  .brand {
    position: absolute;
    left: 295px;
    top: 44px;
    width: 617px;
    text-align: center;
    font-weight: 900;
    font-size: 98px;
    line-height: 1;
    letter-spacing: -1px;
    color: var(--ink);
  }

  .main-nav {
    position: absolute;
    left: 295px;
    top: 158px;
    width: 617px;
    height: 35px;
    display: flex;
    border: 2px solid var(--ink);
  }
  .main-nav a {
    flex: 1;
    display: flex;
    align-items: center;
    justify-content: center;
    font-size: 22px;
    color: var(--ink);
    text-decoration: none;
    border-right: 2px solid var(--ink);
  }
  .main-nav a:last-child { border-right: none; }
  .main-nav a.is-current { color: var(--teal); }

  .contact-title {
    position: absolute;
    left: 295px;
    top: 252px;
    width: 617px;
    text-align: center;
    font-size: 27px;
    font-weight: 700;
    color: var(--teal);
  }

  .field-label {
    position: absolute;
    left: 298px;
    font-size: 23px;
    line-height: 1;
  }
  .field-label .required { color: var(--teal); margin-right: 6px; }
  .field-label--plain { left: 303px; }

  .field-box {
    position: absolute;
    left: 300px;
    width: 612px;
    height: 28px;
    border: 2px solid var(--teal);
    padding: 3px 8px;
    font-size: 17px;
    color: var(--hint);
    line-height: 1.2;
  }
  .field-box--message { height: 160px; padding-top: 6px; }

  .send-button {
    position: absolute;
    left: 300px;
    top: 688px;
    width: 612px;
    height: 28px;
    background: var(--teal);
    text-align: center;
    font-size: 22px;
    font-weight: 700;
    line-height: 28px;
    color: var(--ink);
  }
</style>
</head>
<body>
<div class="page">
  <div class="side-art side-art--left" role="img" aria-label="Vivid abstract acrylic painting in blues, aqua and orange"></div>
  <div class="side-art side-art--right" role="img" aria-label="Vivid abstract acrylic painting in blues, aqua and orange"></div>

  <div class="brand">VividoCanta</div>

  <nav class="main-nav">
    <a href="#">Home</a>
    <a href="#">About</a>
    <a href="#">Portfolio</a>
    <a href="#">Purchases</a>
    <a href="#" class="is-current">Contact</a>
  </nav>

  <h1 class="contact-title">Contact Me</h1>

  <div class="field-label" style="top:288px"><span class="required">*</span>Full Name</div>
  <div class="field-box" style="top:313px">Marla Quenby</div>

  <div class="field-label" style="top:346px"><span class="required">*</span>Email</div>
  <div class="field-box" style="top:372px">MarlaQuenby@inboxmail.example</div>

  <div class="field-label field-label--plain" style="top:405px">Contact Number</div>
  <div class="field-box" style="top:430px">01 5550 0199</div>

  <div class="field-label" style="top:463px"><span class="required">*</span>Message</div>
  <div class="field-box field-box--message" style="top:492px">Message.....</div>

  <div class="send-button">Send Message</div>
</div>
</body>
</html>
```